Oil Field Service company needs professional business cards

Looking to clean up our current company business cards and look a little more professional. Harlow Tubular Services is a US based company that services the oil field. We deal with engineers, managers and oil rigs....................................................................................................................................................................................................................................................................................................................................................................................................

Target Market(s)

Oil and Gas professionals

Industry/Entity Type

Oil And Gas

Contact Information for Business Card

See attached photo as example

Font styles to use
Sans Serif

Colors
ec1f27

Requirements
Must have
• Company Logo, Name, Title, Cell, Office, Fax, Email.
• See attached photo
Nice to have
• External CRT, Internal CRT, Casing Crews, Torque Turn, Laydown Machine
Should not have
• Do not introduce any new pictures and keep it professional looking

```html
<!DOCTYPE html>
<html lang="en">
<head>
<meta charset="utf-8">
<title>Harlow Tubular Services – Business Cards</title>
<link href="https://fonts.googleapis.com/css2?family=Open+Sans:wght@400;600;700;800&display=swap" rel="stylesheet">
<style>
  :root {
    --brand-red: #ec1f27;
    --slate: #44555f;
    --ink: #3a4a54;
    --paper: #ffffff;
    --backdrop: #e9e6e1;
    --muted: #5b6a73;
  }
  * { box-sizing: border-box; margin: 0; padding: 0; }
  html, body {
    width: 1200px; height: 900px; overflow: hidden;
    background: var(--backdrop);
    font-family: "Open Sans", Arial, sans-serif;
  }
  .sheet {
    width: 1200px; height: 900px;
    display: flex; flex-direction: column; align-items: center; justify-content: center;
    gap: 44px;
  }
  .card {
    position: relative;
    width: 600px; height: 343px;
    overflow: hidden;
    box-shadow: 0 4px 14px rgba(0,0,0,.18);
  }
  /* Back side */
  .card--back { background: var(--slate); color: var(--paper); }
  .card--back .wordmark {
    position: absolute; left: 0; right: 0; top: 118px;
    text-align: center; color: var(--paper);
  }
  .wordmark__name {
    font-weight: 800; font-size: 34px; letter-spacing: 2px; text-transform: uppercase;
    display: inline-flex; align-items: center; gap: 12px;
  }
  .wordmark__dot { width: 14px; height: 14px; border-radius: 50%; background: var(--brand-red); display: inline-block; }
  .services {
    position: absolute; left: 0; right: 0; top: 236px;
    text-align: center; font-size: 15px; letter-spacing: .3px; color: #e6ecef;
  }
  /* Front side */
  .card--front { background: var(--paper); color: var(--ink); }
  .card__bands { position: absolute; inset: 0; width: 600px; height: 343px; }
  .person { position: absolute; left: 68px; top: 22px; }
  .person__name { font-size: 17px; font-weight: 700; color: var(--ink); }
  .person__first { color: var(--brand-red); }
  .person__title { font-size: 12.5px; color: var(--muted); margin-top: -2px; }
  .contacts { position: absolute; left: 40px; top: 168px; list-style: none; }
  .contacts li {
    display: flex; align-items: center; gap: 10px;
    font-size: 15px; line-height: 21px; color: var(--ink);
  }
  .contacts svg { width: 11px; height: 11px; flex: none; }
  .card--front .wordmark {
    position: absolute; left: 300px; right: 20px; top: 136px; text-align: center;
    color: var(--ink);
  }
  .card--front .wordmark__name { font-size: 22px; letter-spacing: 1.5px; }
  .card--front .wordmark__dot { width: 11px; height: 11px; }
</style>
</head>
<body>
<main class="sheet">

  <section class="card card--back" aria-label="Card back">
    <div class="wordmark">
      <span class="wordmark__name"><span class="wordmark__dot"></span>Harlow Tubular Services</span>
    </div>
    <p class="services">Laydown Machine | Casing Crew | Mud Tool | Torque Turn</p>
  </section>

  <section class="card card--front" aria-label="Card front">
    <svg class="card__bands" viewBox="0 0 600 343" aria-hidden="true">
      <polygon points="0,12 34,12 22,46 0,46" fill="var(--brand-red)"/>
      <polygon points="38,12 56,12 56,46 26,46" fill="var(--slate)"/>
      <polygon points="0,282 278,282 268,302 0,302" fill="var(--brand-red)"/>
      <polygon points="282,302 600,302 600,343 264,343" fill="var(--slate)"/>
    </svg>

    <div class="person">
      <p class="person__name"><span class="person__first">Wade</span> Kellerson</p>
      <p class="person__title">Area Manager</p>
    </div>

    <ul class="contacts">
      <li>
        <svg viewBox="0 0 12 12"><path d="M2.5 1l2 2.2-1 1.3c.8 1.6 2 2.8 3.5 3.5l1.3-1 2.2 2-1 1.8C5 10.5 1.5 7 .8 2z" fill="var(--brand-red)"/></svg>
        (555) 014-5700
      </li>
      <li>
        <svg viewBox="0 0 12 12"><rect x="3" y="0.8" width="6" height="10.4" rx="1.2" fill="none" stroke="var(--brand-red)" stroke-width="1.3"/></svg>
        (555) 018-7496
      </li>
      <li>
        <svg viewBox="0 0 12 12"><rect x="1" y="5" width="10" height="6" rx="1" fill="var(--brand-red)"/><rect x="3" y="1" width="6" height="4" fill="none" stroke="var(--brand-red)" stroke-width="1.2"/></svg>
        (555) 014-3230
      </li>
      <li>
        <svg viewBox="0 0 12 12"><rect x="0.5" y="2" width="11" height="8" fill="var(--brand-red)"/><path d="M0.8 2.4L6 6.6l5.2-4.2" fill="none" stroke="#fff" stroke-width="1"/></svg>
        wkellerson@harlowtubular.com
      </li>
    </ul>

    <div class="wordmark">
      <span class="wordmark__name"><span class="wordmark__dot"></span>Harlow Tubular Services</span>
    </div>
  </section>

</main>
</body>
</html>
```